Business Card Design

We need a basic, but modern design card. Our business is a local Queanbeyan/Canberra courier service, but can organise interstate delivery if needed. Our fleet ranges from 1 tonne vans to 8 tonne trucks.

Industry/Entity Type

Business

Contact Information for Business Card

Harbourline Freight
14 Tarrant Road
Queanbeyan NSW 2620

Owen Prescott
CEO

Phone: 02 61847315
Fax: 02 61847398
email: owen@harbourlinefreight.com.au

```html
<!DOCTYPE html>
<html lang="en">
<head>
<meta charset="utf-8">
<title>Harbourline Freight – Business Card</title>
<link href="https://fonts.googleapis.com/css2?family=Arimo:ital,wght@0,700;1,400;1,500&display=swap" rel="stylesheet">
<style>
  :root {
    --paper: #eff3f2;
    --mint: #7ff5d2;
    --blue: #2f7cf6;
    --blush: #f3dede;
    --red: #ef3b24;
    --red-deep: #e8281a;
    --brand-blue: #0b3cf0;
    --brand-red: #f02a0a;
    --band: rgba(58, 60, 68, 0.78);
    --band-text: #ffffff;
  }
  html, body {
    margin: 0;
    padding: 0;
    overflow: hidden;
    background: #ffffff;
  }
  .card {
    position: relative;
    width: 1200px;
    height: 706px;
    overflow: hidden;
    background: var(--paper);
    font-family: "Arimo", Arial, sans-serif;
  }
  .backdrop {
    position: absolute;
    inset: 0;
    background: linear-gradient(90deg,
      var(--blue) 0%,
      var(--mint) 12%,
      var(--mint) 22%,
      var(--paper) 38%,
      var(--paper) 66%,
      var(--blush) 76%,
      var(--red) 90%,
      var(--red-deep) 100%);
  }
  .brand {
    position: absolute;
    left: 0;
    right: 0;
    top: 236px;
    display: flex;
    justify-content: center;
    align-items: center;
    gap: 22px;
  }
  .brand-square {
    width: 52px;
    height: 52px;
    background: var(--brand-red);
  }
  .brand-name {
    font-weight: 700;
    font-size: 62px;
    letter-spacing: 1px;
    color: var(--brand-blue);
  }
  .contact-band {
    position: absolute;
    left: 0;
    right: 0;
    top: 498px;
    bottom: 0;
    background: var(--band);
    color: var(--band-text);
    font-style: italic;
    font-weight: 500;
    text-align: center;
  }
  .contact-band p {
    margin: 0;
    position: absolute;
    left: 0;
    right: 0;
    line-height: 1;
    white-space: nowrap;
  }
  .address { top: 20px; font-size: 24px; }
  .person  { top: 56px; font-size: 29px; letter-spacing: 2px; }
  .phone   { top: 96px; font-size: 24px; }
  .fax     { top: 133px; font-size: 24px; }
  .email   { top: 169px; font-size: 24px; }
</style>
</head>
<body>
  <div class="card">
    <div class="backdrop" role="img" aria-label="Decorative background of overlapping translucent facets, mint and blue on the left, blush and red on the right"></div>

    <div class="brand">
      <span class="brand-square"></span>
      <span class="brand-name">Harbourline Freight</span>
    </div>

    <div class="contact-band">
      <p class="address">Harbourline Freight 14 Tarrant Road Queanbeyan NSW 2620</p>
      <p class="person">Owen Prescott</p>
      <p class="phone">CEO Phone: 02 61847315</p>
      <p class="fax">Fax: 02 61847398</p>
      <p class="email">owen@harbourlinefreight.com.au</p>
    </div>
  </div>
</body>
</html>
```